Exklusives Modernes Logo & Visitenkarte Design für Fotografie
Zielgruppe
Fine Art Photography, suche ein exklusives Design. Zielgruppe primär Privatpersonen, gehobene Gesellschaft.
Aufgabenstellung
Sehr hochwertiges Design! Für anspruchsvolle Kunden.
Visitenkarten Design außergewöhnlich bitte!
Vielleicht auch Guerilla-Marketing (Design)
Font: Miso & Jura
Für Visitenkarte:
Wendholm Fine Art Photography
Business Owner
Jonas Emil Wendholm
Office: Birkweg 14, 3651 Oberfelden on the Danube, Austria
Photoatelier: Neuer Platz 9, 3241 Grubau, Austria
Web: jonas-wendholm.example / E-Mail: mail@jonas-wendholm.example
Mobile +43(0) 660 17 38 904 - Austria
Fon: +43 (0) 2758 41 836 - Austria / +46 8 739 215 - Sweden
Fax: +43 (0) 2758 41 836 11

```html
<!DOCTYPE html>
<html lang="en">
<head>
<meta charset="utf-8">
<title>Wendholm Fine Art Photography – Brand &amp; Business Card</title>
<link rel="stylesheet" href="https://fonts.googleapis.com/css2?family=Jura:wght@400;500&family=Open+Sans:wght@400;700&display=swap">
<style>
  :root {
    --stage-grey: #8a8a8a;
    --photo-light: #b9b9b9;
    --photo-mid: #9a9a9a;
    --photo-dark: #4a4a4a;
    --lime: #c9d30a;
    --paper: #f4f4f4;
    --ink: #1d1d1b;
    --white: #ffffff;
  }
  * { margin: 0; padding: 0; box-sizing: border-box; }
  html, body { width: 1119px; height: 1200px; overflow: hidden; }
  body { background: var(--stage-grey); font-family: "Open Sans", Arial, sans-serif; }
  .canvas { position: relative; width: 1119px; height: 1200px; overflow: hidden; background: var(--stage-grey); }

  .portrait-photo {
    position: absolute; left: 239px; top: 0; width: 880px; height: 1200px;
    background:
      radial-gradient(ellipse 40% 45% at 62% 38%, var(--photo-light), transparent 70%),
      linear-gradient(160deg, var(--photo-mid) 0%, #a6a6a6 40%, #6b6b6b 75%, var(--photo-dark) 100%);
  }

  .brand-name {
    position: absolute; font-family: "Jura", sans-serif; font-weight: 500; line-height: 1;
  }
  .brand-name .word { display: block; font-size: 46px; letter-spacing: 1px; }
  .brand-name .tagline { display: block; font-size: 27px; margin-top: 8px; }
  .stage-brand { left: 146px; top: 196px; color: var(--white); }

  .card { position: absolute; background: var(--lime); }
  .card-front { left: 151px; top: 554px; width: 537px; height: 306px; }
  .card-front .brand-name { left: 104px; top: 94px; color: var(--ink); }
  .owner-name {
    position: absolute; left: 134px; top: 250px;
    font-family: "Open Sans", sans-serif; font-weight: 700; font-size: 16px;
    letter-spacing: 2px; color: var(--white);
  }

  .card-back { left: 155px; top: 877px; width: 537px; height: 307px; }
  .contact-panel {
    position: absolute; left: 36px; top: 35px; width: 465px; height: 236px;
    background: var(--paper);
  }
  .contact-list { position: absolute; left: 0; top: 50px; list-style: none; }
  .contact-row { display: flex; align-items: center; height: 18px; font-size: 13px; color: var(--ink); white-space: nowrap; }
  .contact-row.gap { margin-top: 11px; }
  .contact-row + .contact-row { margin-top: 2.5px; }
  .contact-row.gap { margin-top: 11px; }
  .label {
    display: inline-block; background: var(--lime); color: var(--white);
    font-weight: 700; font-size: 12px; letter-spacing: .3px;
    height: 15px; line-height: 15px; padding: 0 12px 0 0; margin-right: 4px;
  }
</style>
</head>
<body>
<main class="canvas">
  <div class="portrait-photo" role="img" aria-label="Black-and-white fine art portrait of a woman with slicked-back hair, hand at her neck"></div>

  <div class="brand-name stage-brand">
    <span class="word">Wendholm</span>
    <span class="tagline">Fine Art Photography</span>
  </div>

  <section class="card card-front" aria-label="Business card front">
    <div class="brand-name">
      <span class="word">Wendholm</span>
      <span class="tagline">Fine Art Photography</span>
    </div>
    <p class="owner-name">Jonas Emil Wendholm</p>
  </section>

  <section class="card card-back" aria-label="Business card back">
    <div class="contact-panel">
      <ul class="contact-list">
        <li class="contact-row"><span class="label" style="width:66px">OFFICE</span>Birkweg 14, 3651 Oberfelden on the Danube, Austria</li>
        <li class="contact-row"><span class="label" style="width:118px">PHOTOATELIER</span>Neuer Platz 9, 3241 Grubau, Austria</li>
        <li class="contact-row gap"><span class="label" style="width:63px">MOBILE</span>+43(0) 660 17 38 904 - Austria</li>
        <li class="contact-row"><span class="label" style="width:40px">FON</span>+43 (0) 2758 41 836 - Austria / +46 8 739 215 - Sweden</li>
        <li class="contact-row"><span class="label" style="width:38px">FAX</span>+43 (0) 2758 41 836 11</li>
        <li class="contact-row"><span class="label" style="width:60px">E-MAIL</span>mail@jonas-wendholm.example</li>
        <li class="contact-row"><span class="label" style="width:42px">WEB</span>jonas-wendholm.example</li>
      </ul>
    </div>
  </section>
</main>
</body>
</html>
```